Plumbing Service Flyer Needed For Swapnook

Plumbing ad needs to be effective (600 by 450 pixels)
Ad must include company name Kestrel Drainworks and phone number 404-555-0183
No URLs, links, or web addresses in your text or image please.

(about us we offer a wide range of plumbing services from emergency plumbing to commercial plumbing services, our master plumbers are ready to handle all jobs, large or small, at anytime during the day or night. Pickup the phone and call us today).

Target Market(s)

DC Metro Area

Industry/Entity Type

Plumbing

Font styles to use
Other font styles liked:
• No preference. Let the designer choose

Colors

Designer to choose colors to be used in the design.

Requirements
Must have
• 1. A bold headline: headline should communicate what my business is all about.
• 2. Great photography
• 3. Discounts or specials
• 4. Call to action
• 5. Key facts: Let consumers know about the product or service (see attached ad)
• 6. Good graphics
Should not have
• No URLs, links, or web addresses in your text or image please.

```html
<!DOCTYPE html>
<html lang="en">
<head>
<meta charset="utf-8">
<title>Kestrel Drainworks – Plumbing Service Flyer</title>
<link rel="stylesheet" href="https://fonts.googleapis.com/css2?family=Arvo:ital,wght@1,700&family=Lato:wght@400;700&family=Montserrat:wght@700;800&family=Roboto+Slab:wght@800;900&display=swap">
<style>
  :root {
    --flame: #ff3d17;
    --crimson: #e8173a;
    --navy: #0f3a93;
    --white: #ffffff;
    --ash: #b9b9b9;
    --shadow: #c9c9c9;
  }
  * { margin: 0; padding: 0; box-sizing: border-box; }
  html, body { width: 900px; height: 1200px; overflow: hidden; background: var(--white); }
  .flyer {
    position: relative; width: 900px; height: 1200px; overflow: hidden;
    background: linear-gradient(#ffffff 0%, #ffffff 70%, #ececec 88%);
    font-family: "Lato", sans-serif;
  }
  .top-band {
    position: absolute; left: 0; top: 0; width: 900px; height: 113px;
    background: var(--flame); color: var(--white);
  }
  .top-band .promise {
    position: absolute; left: 0; width: 740px; top: 22px; text-align: center;
    font-family: "Arvo", serif; font-style: italic; font-weight: 700; font-size: 35px;
  }
  .top-band .same-day {
    position: absolute; left: 0; width: 790px; top: 64px; text-align: center;
    font-family: "Montserrat", sans-serif; font-weight: 700; font-size: 23px;
  }
  .fast-icon { position: absolute; left: 700px; top: 25px; }
  .brand {
    position: absolute; left: 0; width: 900px; top: 118px; text-align: center;
    font-family: "Roboto Slab", serif; font-weight: 900; font-size: 80px; letter-spacing: -2px;
    white-space: nowrap;
  }
  .brand .first { color: var(--crimson); }
  .brand .second { color: var(--navy); }
  .hero-photo {
    position: absolute; left: 560px; top: 235px; width: 340px; height: 815px;
    background: linear-gradient(180deg, #d9dfee 0%, #2f5fc4 35%, #1f4bb0 70%, #c9a56b 85%, #2548a8 100%);
    border-radius: 120px 120px 0 0;
  }
  .bubble { position: absolute; left: 30px; top: 262px; }
  .bubble-text {
    position: absolute; left: 45px; top: 278px; width: 610px; text-align: center;
    color: var(--white); font-size: 16px; line-height: 24px; letter-spacing: -0.3px;
  }
  .tick { position: absolute; left: 55px; top: 405px; }
  .pledge {
    position: absolute; left: 100px; width: 450px; top: 424px; text-align: center;
    color: var(--navy); font-family: "Montserrat", sans-serif; font-weight: 800;
    font-size: 24px; line-height: 29px;
  }
  .services-title {
    position: absolute; left: 58px; top: 502px;
    color: var(--crimson); font-family: "Roboto Slab", serif; font-weight: 800; font-size: 44px;
  }
  .services-box {
    position: absolute; left: 62px; top: 578px; width: 418px; height: 407px;
    background: var(--navy); border-radius: 14px;
    box-shadow: 9px 9px 0 var(--shadow);
    padding: 30px 0 0 26px;
  }
  .services-list { list-style: none; color: var(--white); font-size: 25px; line-height: 31.2px; }
  .services-list li::before { content: "• "; }
  .services-list .more { padding-left: 14px; }
  .cta-tab { position: absolute; left: 0; top: 1004px; }
  .cta-text {
    position: absolute; left: 63px; top: 1012px;
    color: var(--white); font-family: "Arvo", serif; font-weight: 700; font-style: normal; font-size: 24px;
  }
  .phone-band {
    position: absolute; left: 0; top: 1050px; width: 900px; height: 126px;
    background: var(--navy);
  }
  .phone-number {
    position: absolute; left: 0; width: 940px; top: 1046px; text-align: center;
    color: var(--white); font-family: "Montserrat", sans-serif; font-weight: 800;
    font-size: 112px; letter-spacing: -1px;
  }
  .base-strip { position: absolute; left: 0; top: 1176px; width: 900px; height: 24px; background: var(--ash); }
</style>
</head>
<body>
<main class="flyer">
  <header class="top-band">
    <p class="promise">24/7 Plumber at Your Service!</p>
    <p class="same-day">Call us today for same day service.</p>
    <svg class="fast-icon" width="115" height="62" viewBox="0 0 115 62" aria-hidden="true">
      <g stroke="#ffffff" stroke-width="6" stroke-linecap="round" fill="none">
        <line x1="5" y1="12" x2="55" y2="12"/>
        <line x1="20" y1="26" x2="45" y2="26"/>
        <line x1="5" y1="40" x2="45" y2="40"/>
        <line x1="25" y1="54" x2="55" y2="54"/>
        <circle cx="82" cy="34" r="25"/>
        <line x1="76" y1="5" x2="88" y2="5"/>
        <polyline points="72,34 80,42 94,26"/>
      </g>
    </svg>
  </header>

  <h1 class="brand"><span class="first">Kestrel</span> <span class="second">Drainworks</span></h1>

  <div class="hero-photo" role="img" aria-label="Bearded plumber in a blue cap and blue overalls with a tool belt, pointing toward the services list"></div>

  <svg class="bubble" width="640" height="155" viewBox="0 0 640 155" aria-hidden="true">
    <path d="M20 0 H617 A20 20 0 0 1 637 20 V108 A20 20 0 0 1 617 128 H318 L302 153 L286 128 H20 A20 20 0 0 1 0 108 V20 A20 20 0 0 1 20 0 Z" fill="var(--crimson)"/>
  </svg>
  <p class="bubble-text">The best priced any plumbing repair install or remodel. You only need one call for us to handle it all, super fast, always reliable &amp; affordable plumber. Bonded, licensed and insured. We handle fixes, installation, leaks, remodels, new construction and more!</p>

  <svg class="tick" width="90" height="85" viewBox="0 0 90 85" aria-hidden="true">
    <path d="M2 45 L18 36 L32 58 Q55 20 88 2 Q62 30 34 84 Z" fill="var(--crimson)"/>
  </svg>
  <p class="pledge">Do not use a handyman,<br>use a certified plumber like me.</p>

  <h2 class="services-title">Plumbing Services:</h2>
  <section class="services-box">
    <ul class="services-list">
      <li>Plumbing Clogs</li>
      <li>Water Heater Replacement</li>
      <li>Repair and Install Gas Lines</li>
      <li>Remodel your Plumbing</li>
      <li>Flood Repair</li>
      <li>Disposals Repair and Install</li>
      <li>Toilets Install or Replace</li>
      <li>New Piping and Repairs</li>
      <li>New Homes, Old Homes</li>
      <li>Commercial Plumbing</li>
      <li class="more">and a ton more...</li>
    </ul>
  </section>

  <svg class="cta-tab" width="580" height="47" viewBox="0 0 580 47" aria-hidden="true">
    <path d="M0 0 H545 Q555 0 560 10 L578 47 H0 Z" fill="var(--flame)"/>
  </svg>
  <p class="cta-text">Pickup the phone and call us today!</p>

  <div class="phone-band"></div>
  <p class="phone-number">404-555-0183</p>
  <div class="base-strip"></div>
</main>
</body>
</html>
```